Bright Towns Alliance PowerPoint Design Template and Sample Deck

The Bright Towns Alliance is an international organization that seeks to improve the livability, workability and sustainability of the world’s cities.
We seek a versatile PowerPoint design template with 10 slide types plus a “self-documenting” sample deck. Your design will be used in keynote speeches and workshops around the world.
After the contest is completed, we will ask the winning designer to add 10-20 additional slide types for $75 per slide. We also seek a long-term relationship whereby we can request “custom” slides and/or ask the designer to touch up the slides we build to make them better.
FILES. We have uploaded several files:
1. BRIGHT TOWNS ALLIANCE DESIGN CONTEST NOTES.docx with full instructions.
2. PALETTE. Shows our official colors.
3 LOGOS. Several individual files with different variations of our logo. Some with our motto, some without.
2. SAMPLE SLIDES. Because we were unable to successfully upload our sample deck, we are making it available via this FileCrate link:
https://www.filecrate-example.net/s/k7qvmr2tn8wzd4h/The%20Bright%20Towns%20Alliance%20Design%20Contest%20Notes.docx?dl=0
Target Market(s)
Mayors, department heads, CIOs, senior executives from technology companies
Industry/Entity Type
Information Technology
Colors
Designer to choose colors to be used in the design.
Requirements
Must have
- Please see uploaded Word document for requirements, nice to haves and should not haves and uploaded palette for color preferences.
Nice to have
- see above
Should not have
- see above

```html
<!DOCTYPE html>
<html lang="en">
<head>
<meta charset="utf-8">
<title>Bright Towns Alliance – Slide Template Set</title>
<link href="https://fonts.googleapis.com/css2?family=Mulish:ital,wght@0,400;0,600;0,700;0,800;1,600&family=Playfair+Display:ital,wght@1,700&display=swap" rel="stylesheet">
<style>
:root{
  --blue:#1f4e93;
  --navy:#12306a;
  --orange:#f7941d;
  --orange-dark:#e07c0c;
  --ink:#2b2b2b;
  --grey-bg:#c8c8c8;
  --map:#c4c4c4;
  --red:#e2412d;
  --green:#7d9c34;
  --purple:#7a4c9c;
  --sky:#2a76c0;
  --silver:#9b9b9b;
}
*{margin:0;padding:0;box-sizing:border-box}
html,body{width:1200px;height:2269px;overflow:hidden;background:var(--grey-bg);font-family:"Mulish",sans-serif;color:var(--ink)}
.canvas{position:relative;width:1200px;height:2269px}
.slide{position:absolute;width:535px;height:400px;background:#fff;overflow:hidden;box-shadow:0 4px 10px rgba(0,0,0,.28)}
.col-l{left:40px}.col-r{left:625px}
.row1{top:48px}.row2{top:491px}.row3{top:924px}.row4{top:1360px}.row5{top:1797px}

/* header */
.head-bar{position:absolute;left:0;top:0;width:470px;height:40px;background:var(--blue);clip-path:polygon(0 0,100% 0,95% 100%,0 100%)}
.head-stripe{position:absolute;left:0;top:40px;width:310px;height:4px;background:var(--orange);clip-path:polygon(0 0,100% 0,97% 100%,0 100%)}
.head-title{position:absolute;left:70px;top:9px;color:#fff;font-size:19px;font-weight:600;letter-spacing:.3px;white-space:nowrap}
.motto-tag{position:absolute;left:345px;top:0;width:150px;height:44px;background:var(--navy);clip-path:polygon(16% 0,100% 0,84% 100%,0 100%)}
.motto{position:absolute;left:384px;top:6px;color:#fff;font-size:7px;font-style:italic;font-weight:600;line-height:10px;letter-spacing:.3px}
.slide-no{position:absolute;right:18px;top:52px;color:var(--orange);font-size:10px}

/* footer */
.foot{position:absolute;left:0;bottom:0;width:100%;height:28px;background:var(--orange)}
.foot-blue{position:absolute;left:0;bottom:0;width:260px;height:28px;background:var(--blue);clip-path:polygon(0 0,100% 0,88% 100%,0 100%)}
.foot-navy{position:absolute;left:0;bottom:0;width:40px;height:28px;background:var(--navy);clip-path:polygon(0 0,100% 0,60% 100%,0 100%)}
.brand{position:absolute;left:60px;bottom:7px;color:#fff;font-size:13px;font-weight:600;white-space:nowrap}
.url{position:absolute;left:290px;bottom:8px;color:var(--navy);font-size:10px;font-weight:700}

.photo{position:absolute}
p,li{font-size:9px;line-height:12px}

/* slide 1 chevrons */
.chev{position:absolute;width:150px;height:108px;background:var(--blue);color:#fff;clip-path:polygon(0 0,86% 0,100% 50%,86% 100%,0 100%,10% 50%);padding:10px 26px 0 22px}
.chev.first{clip-path:polygon(0 0,86% 0,100% 50%,86% 100%,0 100%);border-radius:10px 0 0 10px;padding-left:14px}
.chev.active{background:var(--orange)}
.chev.active p{font-weight:700}
.chev h3{font-size:13px;font-weight:600;margin-bottom:4px}
.chev.active h3{color:var(--navy);font-weight:800}
.chev p{font-size:7.5px;line-height:9.5px}

/* slide 2 bands */
.band{position:absolute;left:20px;width:460px;color:#fff;padding:8px 16px}
.band h3{font-size:12px;font-weight:600;margin-bottom:3px}
.band p{font-size:8px;line-height:10px;width:400px}
.band.blue{top:150px;height:56px;background:rgba(24,60,130,.92);clip-path:polygon(0 0,100% 0,96% 100%,0 100%)}
.band.orange{top:278px;height:56px;background:rgba(247,148,29,.95);clip-path:polygon(0 0,100% 0,96% 100%,0 100%)}
.band.blue h3{color:var(--orange)}
.band.orange h3{color:var(--navy)}

/* slide 3 quote */
.quote{position:absolute;right:40px;top:28px;width:330px;text-align:right;color:#fff;font-family:"Playfair Display",serif;font-style:italic;font-weight:700;font-size:22px;line-height:28px}
.quote-by{position:absolute;right:40px;top:96px;color:#fff;font-size:16px;font-weight:700}

/* slide 4 */
.intro{position:absolute;left:26px;top:66px;width:485px;font-size:8.5px;line-height:11px}
.tab{position:absolute;height:20px;background:var(--orange);color:#fff;font-size:11px;font-weight:700;padding:3px 10px;clip-path:polygon(0 0,100% 0,94% 100%,0 100%)}
.bullets{position:absolute;list-style:none}
.bullets li{position:relative;padding-left:14px;margin-bottom:8px;font-size:8px;line-height:10px}
.bullets li::before{content:"";position:absolute;left:0;top:2px;border-left:6px solid var(--navy);border-top:4px solid transparent;border-bottom:4px solid transparent}

/* slide 5 */
.dot{position:absolute;border-radius:50%;display:flex;align-items:center;justify-content:center;font-weight:700}
.dot.fill{background:var(--orange);color:#fff}
.dot.ring{border:2px solid var(--orange);color:var(--orange);background:#fff}
.stat-txt{position:absolute;font-size:8px;line-height:11px}
.num-o{position:absolute;color:var(--orange);font-weight:400}
.pill{position:absolute;border:2px solid var(--orange);border-radius:14px;color:var(--blue);font-weight:600;font-size:14px;text-align:center;padding:3px 0}
.hl{border:1px solid var(--orange);border-radius:6px;color:var(--blue);padding:0 2px;line-height:9px;display:inline-block}

/* slide 6 */
.desc-h{position:absolute;left:28px;top:58px;color:var(--orange);font-size:13px;font-weight:600}
.desc{position:absolute;left:28px;top:76px;width:480px;font-size:8.5px;line-height:11px}

/* slide 7 */
.twocol{position:absolute;left:78px;top:80px;width:362px;height:192px;border:1px solid #bbb}
.twocol .divider{position:absolute;left:180px;top:0;width:1px;height:100%;background:#bbb}
.tab-wide{position:absolute;top:-12px;height:24px;width:186px;background:var(--orange);color:#fff;font-size:12px;font-weight:700;padding:4px 10px}

/* slide 8 */
.pic-title{position:absolute;top:78px;font-size:12px;font-weight:700}
.strip{position:absolute;left:28px;top:222px;width:507px;height:68px;background:var(--orange);color:#fff;font-size:11px;font-weight:600;line-height:15px;text-align:center;padding:14px 24px 0 50px;clip-path:polygon(0 0,100% 0,100% 100%,4% 100%)}

/* slide 9 */
.tl-card{position:absolute;top:131px;width:76px;height:112px;background:#eef2f8;padding:8px 6px}
.tl-card svg{display:block;margin:0 auto 6px}
.tl-card p{font-size:6.5px;line-height:8.5px}
.tl-tab{position:absolute;top:246px;width:76px;height:20px;color:#fff;font-size:8px;text-align:center;line-height:20px}
.tl-line{position:absolute;left:16px;top:305px;width:500px;height:2px;background:#d0d0d0}
.tl-dot{position:absolute;top:291px;width:28px;height:28px;border-radius:50%;color:#fff;font-size:7px;text-align:center;line-height:28px}

/* slide 10 */
.step{position:absolute;width:144px;height:100px;background:var(--orange);border-radius:8px;color:#fff;padding:8px 10px}
.step h4{font-size:10px;font-weight:600;margin-bottom:3px}
.step p{font-size:7.5px;line-height:9.5px;width:84px}
.step .sep{position:absolute;left:100px;top:12px;width:1px;height:76px;background:rgba(255,255,255,.7)}
.step .num{position:absolute;left:108px;top:34px;font-size:20px}
.step svg{position:absolute;left:112px;top:30px}
.step-tab{position:absolute;top:-8px;left:0;width:24px;height:10px;background:var(--orange-dark);clip-path:polygon(0 100%,40% 0,100% 0,100% 100%)}
</style>
</head>
<body>
<div class="canvas">

<section class="slide col-l row1">
  <div class="head-bar"></div><div class="head-stripe"></div><div class="motto-tag"></div>
  <div class="head-title">1. PROGRESSIVE AGENDA</div>
  <div class="motto">CONNECTED /<br>RESILIENT /<br>INCLUSIVE</div>
  <div class="slide-no">slide 01</div>
  <div class="chev first" style="left:40px;top:92px"><h3>SECTION 1</h3><p>Lorem ipsum dolor sit amet, consectetur adipiscing elit. In at risus lorem. Ut tempor maximus leo, quis tristique felis.</p></div>
  <div class="chev active" style="left:180px;top:92px"><h3>SECTION 2</h3><p>Lorem ipsum dolor sit amet, consectetur elit. In at risus lorem. Ut tempor.</p></div>
  <div class="chev" style="left:320px;top:92px"><h3>SECTION 3</h3><p>Lorem ipsum dolor sit amet, consectetur adipiscing elit. In at risus lorem. Ut tempor.</p></div>
  <div class="chev first" style="left:40px;top:226px"><h3>SECTION 4</h3><p>Lorem ipsum dolor sit amet, consectetur adipiscing elit. In at risus lorem. Ut tempor.</p></div>
  <div class="chev" style="left:180px;top:226px"><h3>SECTION 5</h3><p>Lorem ipsum dolor sit amet, consectetur adipiscing elit. In at risus lorem. Ut tempor.</p></div>
  <div class="chev" style="left:320px;top:226px"><h3>SECTION 6</h3><p>Lorem ipsum dolor sit amet, consectetur adipiscing elit. In at risus lorem. Ut tempor.</p></div>
  <div class="foot"></div><div class="foot-blue"></div><div class="foot-navy"></div>
  <div class="brand">Bright Towns Alliance</div><div class="url">www.brighttownsalliance.org</div>
</section>

<section class="slide col-r row1">
  <div class="photo" role="img" aria-label="Night city skyline with light trails on a highway" style="left:0;top:0;width:535px;height:400px;background:linear-gradient(160deg,#1b2a4a 0%,#3a4a6e 35%,#8a6a50 60%,#d9b070 75%,#3a3448 100%)"></div>
  <div class="head-bar"></div><div class="head-stripe"></div><div class="motto-tag"></div>
  <div class="head-title">2. FULL BLEED</div>
  <div class="motto">CONNECTED /<br>RESILIENT /<br>INCLUSIVE</div>
  <div class="slide-no" style="color:#fff">slide 02</div>
  <div class="band blue"><h3>TITLE 1</h3><p>Lorem ipsum dolor sit amet, consectetur adipiscing elit. In at risus lorem. Ut tempor maximus leo, quis tristique felis rutrum vel. Fusce sed justo purus. Duis ut ante nulla.</p></div>
  <div class="band orange"><h3>TITLE 2</h3><p>Lorem ipsum dolor sit amet, consectetur adipiscing elit. In at risus lorem. Ut tempor maximus leo, quis tristique felis rutrum vel. Fusce sed justo purus. Duis ut ante nulla.</p></div>
  <div class="foot"></div><div class="foot-blue"></div><div class="foot-navy"></div>
  <div class="brand">Bright Towns Alliance</div><div class="url">www.brighttownsalliance.org</div>
</section>

<section class="slide col-l row2">
  <div class="photo" role="img" aria-label="Earth at night seen from orbit with glowing city lights" style="left:0;top:0;width:535px;height:400px;background:radial-gradient(ellipse at 55% 75%,#a0641c 0%,#4a3a2a 30%,#1d2a38 60%,#05080c 100%)"></div>
  <div class="quote">“ Lorem ipsum dolor sit amet, consectetur adipiscing elit. ”</div>
  <div class="quote-by">by John Doe</div>
  <div class="foot"></div><div class="foot-blue"></div><div class="foot-navy"></div>
  <div class="brand">Bright Towns Alliance</div><div class="url">www.brighttownsalliance.org</div>
</section>

<section class="slide col-r row2">
  <div class="head-bar"></div><div class="head-stripe"></div><div class="motto-tag"></div>
  <div class="head-title">4. TEXT HEAVY</div>
  <div class="motto">CONNECTED /<br>RESILIENT /<br>INCLUSIVE</div>
  <div class="slide-no">slide 04</div>
  <p class="intro">In fermentum hendrerit nisl, a commodo enim fringilla quis. Vivamus fermentum ornare viverra. Praesent dictum a tellus nec volutpat. Pellentesque in nibh quis magna euismod rhoncus. Donec id volutpat turpis. Mauris finibus nisi id tempor mattis. Curabitur at ipsum eros. Vivamus quis augue ut ex iaculis tincidunt eu non augue. Quisque quis nisl cursus, auctor nunc sed, interdum massa. Integer eget mauris urna.</p>
  <div class="tab" style="left:32px;top:141px;width:130px">TITLE 1</div>
  <div class="tab" style="left:208px;top:141px;width:130px">TITLE 2</div>
  <ul class="bullets" style="left:32px;top:172px;width:165px">
    <li>In fermentum hendrerit nisl, a commodo enim fringilla quis.</li>
    <li>In fermentum hendrerit nisl, a commodo enim fringilla quis. Vivamus fermentum ornare</li>
    <li>In fermentum hendrerit nisl, a commodo enim fringilla quis.</li>
    <li>In fermentum hendrerit nisl, a</li>
    <li>In fermentum hendrerit nisl, a commodo enim fringilla quis. Vivamus fermentum ornare viverra. Praesent dictum a tellus</li>
  </ul>
  <ul class="bullets" style="left:208px;top:172px;width:160px">
    <li>In fermentum hendrerit nisl, a</li>
    <li>In fermentum hendrerit nisl, a</li>
    <li>In fermentum hendrerit nisl, a commodo enim fringilla quis.</li>
    <li>In fermentum hendrerit nisl, a commodo enim fringilla quis. Vivamus fermentum ornare viverra. Praesent dictum a tellus</li>
    <li>In fermentum hendrerit nisl, a commodo enim fringilla quis. Vivamus fermentum ornare</li>
  </ul>
  <div class="photo" role="img" aria-label="Worker in a red hard hat checking equipment" style="left:375px;top:157px;width:104px;height:104px;border-radius:50%;background:linear-gradient(135deg,#e8e8ea 0%,#b9c0c8 45%,#c0392b 70%,#6b4a3a 100%)"></div>
  <div class="foot"></div><div class="foot-blue"></div><div class="foot-navy"></div>
  <div class="brand">Bright Towns Alliance</div><div class="url">www.brighttownsalliance.org</div>
</section>

<section class="slide col-l row3">
  <div class="head-bar"></div><div class="head-stripe"></div><div class="motto-tag"></div>
  <div class="head-title">5. STATISTICS HEAVY</div>
  <div class="motto">CONNECTED /<br>RESILIENT /<br>INCLUSIVE</div>
  <div class="slide-no">slide 05</div>
  <div class="dot fill" style="left:40px;top:80px;width:26px;height:26px;font-size:8px">60%</div>
  <p class="stat-txt" style="left:74px;top:87px">Lorem ipsum dolor sit amet, consectetur adipiscing elit. In at risus lorem</p>
  <div class="dot ring" style="left:382px;top:78px;width:28px;height:28px;font-size:8px">40%</div>
  <p class="stat-txt" style="left:416px;top:87px">ipsum dolor sit amet.</p>
  <p class="stat-txt" style="left:40px;top:128px">Lorem ipsum dolor sit amet, consectetur adipiscing elit. In at risus lorem</p>
  <div class="num-o" style="left:378px;top:120px;font-size:18px">25,000</div>
  <svg style="position:absolute;left:18px;top:132px" width="60" height="160"><path d="M4 8 V152 M4 8 H20 M4 152 H20" stroke="#f7941d" stroke-width="1.5" fill="none"/></svg>
  <div class="dot fill" style="left:62px;top:160px;width:106px;height:106px;flex-direction:column;font-weight:400;text-align:center">
    <span style="font-size:17px">35,800</span>
    <span style="font-size:7px;line-height:9px;width:78px;margin-top:3px">In fermentum hendrerit nisl, a commodo enim fringilla quis. Vivamus fermentum ornare</span>
  </div>
  <div class="num-o" style="left:180px;top:172px;font-size:56px;line-height:60px">9000</div>
  <p class="stat-txt" style="left:328px;top:184px;width:185px">In fermentum hendrerit nisl, a commodo enim fringilla quis. Vivamus fermentum ornare viverra. Praesent dictum a tellus nec volutpat. Pellentesque in nibh quis</p>
  <p class="stat-txt" style="left:180px;top:242px">In fermentum hendrerit nisl, a commodo enim fringilla quis</p>
  <div class="dot ring" style="left:424px;top:234px;width:26px;height:26px;font-size:8px">90%</div>
  <p class="stat-txt" style="left:456px;top:242px">risus lorem</p>
  <div class="pill" style="left:40px;top:290px;width:126px">10,000,000</div>
  <p class="stat-txt" style="left:180px;top:284px;width:180px">In fermentum hendrerit nisl, a commodo enim fringilla quis. <span class="hl">30,000</span> ornare viverra. Praesent dictum a tellus nec volutpat. Pellentesque in nibh quis</p>
  <div class="dot fill" style="left:372px;top:268px;width:36px;height:36px;font-size:11px;font-weight:400">60%</div>
  <div class="dot fill" style="left:412px;top:268px;width:36px;height:36px;font-size:11px;font-weight:400">20%</div>
  <div class="dot fill" style="left:452px;top:268px;width:36px;height:36px;font-size:11px;font-weight:400">20%</div>
  <p class="stat-txt" style="left:372px;top:308px;width:36px;font-size:5px;line-height:6px;text-align:center">In fermen- tum nisl, a commodo enim</p>
  <p class="stat-txt" style="left:412px;top:308px;width:36px;font-size:5px;line-height:6px;text-align:center">In fermen- tum nisl, a commodo enim</p>
  <p class="stat-txt" style="left:452px;top:308px;width:36px;font-size:5px;line-height:6px;text-align:center">In fermen- tum nisl, a commodo enim</p>
  <div class="foot"></div><div class="foot-blue"></div><div class="foot-navy"></div>
  <div class="brand">Bright Towns Alliance</div><div class="url">www.brighttownsalliance.org</div>
</section>

<section class="slide col-r row3">
  <div class="head-bar"></div><div class="head-stripe"></div><div class="motto-tag"></div>
  <div class="head-title">6. WORLD MAP</div>
  <div class="motto">CONNECTED /<br>RESILIENT /<br>INCLUSIVE</div>
  <div class="slide-no">slide 06</div>
  <div class="desc-h">DESCRIPTION</div>
  <p class="desc">Lorem ipsum dolor sit amet, consectetur adipiscing elit. In at risus lorem. Ut tempor maximus leo, quis tristique felis rutrum vel. Fusce sed justo purus. Lorem ipsum dolor sit amet, consectetur adipiscing elit. In at risus lorem. Ut tempor maximus leo, quis tristique felis rutrum vel. Fusce sed justo purus.</p>
  <div class="photo" role="img" aria-label="Grey world map with two highlighted city markers" style="left:24px;top:124px;width:490px;height:216px;background:linear-gradient(180deg,#d2d2d2,var(--map));border-radius:40px 60px 30px 50px"></div>
  <div class="foot"></div><div class="foot-blue"></div><div class="foot-navy"></div>
  <div class="brand">Bright Towns Alliance</div><div class="url">www.brighttownsalliance.org</div>
</section>

<section class="slide col-l row4">
  <div class="head-bar"></div><div class="head-stripe"></div><div class="motto-tag"></div>
  <div class="head-title">7. TWO-COLUMN</div>
  <div class="motto">CONNECTED /<br>RESILIENT /<br>INCLUSIVE</div>
  <div class="slide-no">slide 07</div>
  <div class="twocol">
    <div class="divider"></div>
    <div class="tab-wide" style="left:-4px">TITLE 1</div>
    <div class="tab-wide" style="left:180px">TITLE 2</div>
    <ul class="bullets" style="left:8px;top:24px;width:166px">
      <li>Lorem ipsum dolor sit amet, consectetur adipiscing elit. In at risus lorem. Ut tempor maximus leo, quis tristique felis rutrum vel. Fusce sed justo purus.</li>
      <li>Lorem ipsum dolor sit amet, consectetur adipiscing elit. In at risus lorem. Ut</li>
      <li>Lorem ipsum dolor sit amet, consectetur adipiscing elit. In at risus lorem. Ut tempor maximus leo, quis tristique felis</li>
    </ul>
    <ul class="bullets" style="left:188px;top:24px;width:166px">
      <li>Lorem ipsum dolor sit amet, consectetur adipiscing elit. In at risus lorem. Ut tempor maximus leo, quis tristique felis rutrum vel. Fusce sed justo purus.</li>
      <li>Lorem ipsum dolor sit amet, consectetur adipiscing elit. In at risus lorem. Ut</li>
      <li>Lorem ipsum dolor sit amet, consectetur adipiscing elit. In at risus lorem. Ut tempor maximus leo, quis tristique felis</li>
    </ul>
  </div>
  <svg style="position:absolute;left:104px;top:288px" width="150" height="72" aria-label="Rising bar chart">
    <rect x="2" y="54" width="9" height="10" fill="#e2412d"/><rect x="16" y="50" width="9" height="14" fill="#f26a2a"/>
    <rect x="30" y="45" width="9" height="19" fill="#f7941d"/><rect x="44" y="40" width="9" height="24" fill="#f4c430"/>
    <rect x="58" y="34" width="9" height="30" fill="#9cc43a"/><rect x="72" y="27" width="9" height="37" fill="#5fb85a"/>
    <rect x="86" y="19" width="9" height="45" fill="#3fb3a8"/><rect x="100" y="11" width="9" height="53" fill="#3a9ad9"/>
    <rect x="114" y="3" width="9" height="61" fill="#2a76c0"/>
    <line x1="0" y1="66" x2="128" y2="66" stroke="#999" stroke-width="1"/>
  </svg>
  <div class="photo" role="img" aria-label="Hand touching a glowing network of connected people icons" style="left:256px;top:285px;width:168px;height:87px;background:radial-gradient(circle at 40% 40%,#e9d9a0 0%,#3a6aa8 35%,#12306a 100%)"></div>
  <div class="foot"></div><div class="foot-blue"></div><div class="foot-navy"></div>
  <div class="brand">Bright Towns Alliance</div><div class="url">www.brighttownsalliance.org</div>
</section>

<section class="slide col-r row4">
  <div class="head-bar"></div><div class="head-stripe"></div><div class="motto-tag"></div>
  <div class="head-title">8. TWO PICTURES</div>
  <div class="motto">CONNECTED /<br>RESILIENT /<br>INCLUSIVE</div>
  <div class="slide-no">slide 08</div>
  <div class="pic-title" style="left:40px">TITLE 1</div>
  <div class="pic-title" style="left:296px">TITLE 2</div>
  <div class="photo" role="img" aria-label="Conference audience seated in rows" style="left:40px;top:104px;width:216px;height:118px;background:linear-gradient(180deg,#5d6a7e 0%,#8a7d72 50%,#2e3440 100%)"></div>
  <div class="photo" role="img" aria-label="Worker in a red hard hat at a control panel" style="left:296px;top:104px;width:208px;height:118px;background:linear-gradient(120deg,#dfe3e8 0%,#b0b8c2 50%,#c0392b 75%,#5a4032 100%)"></div>
  <div class="strip">Lorem ipsum dolor sit amet, consectetur adipiscing elit. Nullam at eros et eros faucibus placerat. Nam vel arcu at justo condimentum blandit.</div>
  <div class="foot"></div><div class="foot-blue"></div><div class="foot-navy"></div>
  <div class="brand">Bright Towns Alliance</div><div class="url">www.brighttownsalliance.org</div>
</section>

<section class="slide col-l row5">
  <div class="head-bar"></div><div class="head-stripe"></div><div class="motto-tag"></div>
  <div class="head-title">9. TIMELINE</div>
  <div class="motto">CONNECTED /<br>RESILIENT /<br>INCLUSIVE</div>
  <div class="slide-no">slide 09</div>
  <div class="tl-line"></div>
  <div class="tl-card" style="left:16px"><svg width="22" height="20"><rect x="1" y="3" width="20" height="16" rx="2" fill="none" stroke="#1f4e93" stroke-width="1.6"/><line x1="1" y1="8" x2="21" y2="8" stroke="#1f4e93" stroke-width="1.6"/><path d="M6 1v4M16 1v4M5 11h2M10 11h2M15 11h2M5 15h2M10 15h2M15 15h2" stroke="#1f4e93" stroke-width="1.6"/></svg><p>Lorem ipsum dolor sit amet, consecte- tur adipiscing elit. Nullam at eros et eros faucibus</p></div>
  <div class="tl-card" style="left:101px"><svg width="22" height="20"><rect x="1" y="3" width="20" height="16" rx="2" fill="none" stroke="#1f4e93" stroke-width="1.6"/><line x1="1" y1="8" x2="21" y2="8" stroke="#1f4e93" stroke-width="1.6"/><path d="M6 1v4M16 1v4M5 11h2M10 11h2M15 11h2M5 15h2M10 15h2M15 15h2" stroke="#1f4e93" stroke-width="1.6"/></svg><p>Lorem ipsum dolor sit amet, consecte- tur adipiscing elit. Nullam at eros et eros faucibus</p></div>
  <div class="tl-card" style="left:186px"><svg width="22" height="20"><rect x="1" y="3" width="20" height="16" rx="2" fill="none" stroke="#1f4e93" stroke-width="1.6"/><line x1="1" y1="8" x2="21" y2="8" stroke="#1f4e93" stroke-width="1.6"/><path d="M6 1v4M16 1v4M5 11h2M10 11h2M15 11h2M5 15h2M10 15h2M15 15h2" stroke="#1f4e93" stroke-width="1.6"/></svg><p>Lorem ipsum dolor sit amet, consecte- tur adipiscing elit. Nullam at eros et eros faucibus</p></div>
  <div class="tl-card" style="left:271px"><svg width="22" height="20"><rect x="1" y="3" width="20" height="16" rx="2" fill="none" stroke="#1f4e93" stroke-width="1.6"/><line x1="1" y1="8" x2="21" y2="8" stroke="#1f4e93" stroke-width="1.6"/><path d="M6 1v4M16 1v4M5 11h2M10 11h2M15 11h2M5 15h2M10 15h2M15 15h2" stroke="#1f4e93" stroke-width="1.6"/></svg><p>Lorem ipsum dolor sit amet, consecte- tur adipiscing elit. Nullam at eros et eros faucibus</p></div>
  <div class="tl-card" style="left:356px"><svg width="22" height="20"><rect x="1" y="3" width="20" height="16" rx="2" fill="none" stroke="#1f4e93" stroke-width="1.6"/><line x1="1" y1="8" x2="21" y2="8" stroke="#1f4e93" stroke-width="1.6"/><path d="M6 1v4M16 1v4M5 11h2M10 11h2M15 11h2M5 15h2M10 15h2M15 15h2" stroke="#1f4e93" stroke-width="1.6"/></svg><p>Lorem ipsum dolor sit amet, consecte- tur adipiscing elit. Nullam at eros et eros faucibus</p></div>
  <div class="tl-card" style="left:441px"><svg width="22" height="20"><rect x="1" y="3" width="20" height="16" rx="2" fill="none" stroke="#1f4e93" stroke-width="1.6"/><line x1="1" y1="8" x2="21" y2="8" stroke="#1f4e93" stroke-width="1.6"/><path d="M6 1v4M16 1v4M5 11h2M10 11h2M15 11h2M5 15h2M10 15h2M15 15h2" stroke="#1f4e93" stroke-width="1.6"/></svg><p>Lorem ipsum dolor sit amet, consecte- tur adipiscing elit. Nullam at eros et eros faucibus</p></div>
  <div class="tl-tab" style="left:16px;background:var(--orange)">TITLE</div>
  <div class="tl-tab" style="left:101px;background:var(--red)">TITLE</div>
  <div class="tl-tab" style="left:186px;background:var(--green)">TITLE</div>
  <div class="tl-tab" style="left:271px;background:var(--purple)">TITLE</div>
  <div class="tl-tab" style="left:356px;background:var(--sky)">TITLE</div>
  <div class="tl-tab" style="left:441px;background:var(--silver)">TITLE</div>
  <div class="tl-dot" style="left:16px;background:var(--orange)">JAN</div>
  <div class="tl-dot" style="left:101px;background:var(--red)">FEB</div>
  <div class="tl-dot" style="left:186px;background:var(--green)">MAR</div>
  <div class="tl-dot" style="left:271px;background:var(--purple)">APR</div>
  <div class="tl-dot" style="left:356px;background:var(--sky)">MAY</div>
  <div class="tl-dot" style="left:441px;background:var(--silver)">JUN</div>
  <div class="foot"></div><div class="foot-blue"></div><div class="foot-navy"></div>
  <div class="brand">Bright Towns Alliance</div><div class="url">www.brighttownsalliance.org</div>
</section>

<section class="slide col-r row5">
  <div class="head-bar"></div><div class="head-stripe"></div><div class="motto-tag"></div>
  <div class="head-title">10.&nbsp; LINEAR PROCESS</div>
  <div class="motto">CONNECTED /<br>RESILIENT /<br>INCLUSIVE</div>
  <div class="slide-no">slide 10</div>
  <div class="step" style="left:35px;top:96px"><div class="step-tab"></div><h4>TITLE</h4><p>Lorem ipsum dolor sit amet, consectetur adipiscing elit. Nullam at eros et eros faucibus placerat. Nam</p><div class="sep"></div><span class="num">1</span><svg width="20" height="36"><path d="M4 2 L18 18 L4 34" stroke="#fff" stroke-width="2" fill="none"/></svg></div>
  <div class="step" style="left:198px;top:96px"><div class="step-tab"></div><h4>TITLE</h4><p>Lorem ipsum dolor sit amet, consectetur adipiscing elit. Nullam at eros et eros faucibus placerat. Nam</p><div class="sep"></div><span class="num">2</span><svg width="20" height="36"><path d="M4 2 L18 18 L4 34" stroke="#fff" stroke-width="2" fill="none"/></svg></div>
  <div class="step" style="left:361px;top:96px"><div class="step-tab"></div><h4>TITLE</h4><p>Lorem ipsum dolor sit amet, consectetur adipiscing elit. Nullam at eros et eros faucibus placerat. Nam</p><div class="sep"></div><span class="num">3</span><svg width="20" height="36"><path d="M4 2 L18 18 L4 34" stroke="#fff" stroke-width="2" fill="none"/></svg></div>
  <div class="step" style="left:35px;top:237px"><div class="step-tab"></div><h4>TITLE</h4><p>Lorem ipsum dolor sit amet, consectetur adipiscing elit. Nullam at eros et eros faucibus placerat. Nam</p><div class="sep"></div><span class="num">4</span><svg width="20" height="36"><path d="M4 2 L18 18 L4 34" stroke="#fff" stroke-width="2" fill="none"/></svg></div>
  <div class="step" style="left:198px;top:237px"><div class="step-tab"></div><h4>TITLE</h4><p>Lorem ipsum dolor sit amet, consectetur adipiscing elit. Nullam at eros et eros faucibus placerat. Nam</p><div class="sep"></div><span class="num">5</span><svg width="20" height="36"><path d="M4 2 L18 18 L4 34" stroke="#fff" stroke-width="2" fill="none"/></svg></div>
  <div class="step" style="left:361px;top:237px"><div class="step-tab"></div><h4>TITLE</h4><p>Lorem ipsum dolor sit amet, consectetur adipiscing elit. Nullam at eros et eros faucibus placerat. Nam</p><div class="sep"></div><span class="num">6</span><svg width="20" height="36"><path d="M4 2 L18 18 L4 34" stroke="#fff" stroke-width="2" fill="none"/></svg></div>
  <div class="foot"></div><div class="foot-blue"></div><div class="foot-navy"></div>
  <div class="brand">Bright Towns Alliance</div><div class="url">www.brighttownsalliance.org</div>
</section>

</div>
</body>
</html>
```